Business card for my new company (Accounting firm)

I need a business card for my new business Corvane Advisory and Ledger SA. Our services are accounting, tax, audit and financial management. Our customers are small companies, start-ups and new companies. The final design has to show financial security, trust and growth. Please find our logo attached to the business card. Text for the business card: Corvane Advisory and Ledger SA Tomas da Varela Director and Founder Certified Accountant Tel. 022 418 27 35 tv@corvaneconseil.ch www.corvaneconseil.ch Rue des Vergers-Bleus 14 1201 Geneva
Target Market(s)
Our customers are small companies, start-ups and new companies.
Industry/Entity Type
Finance And Accounting
Contact Information for Business Card
Corvane Conseil et Registre SA
Tomas da Varela
Directeur et Fondateur
Expert-comptable diplômé
Tél. 022 418 27 35
tv@corvaneconseil.ch
www.corvaneconseil.ch
Rue des Vergers-Bleus 14
1201 Genève

```html
<!DOCTYPE html>
<html lang="fr">
<head>
<meta charset="utf-8">
<title>Corvane Conseil et Registre SA — Cartes de visite</title>
<link rel="stylesheet" href="https://fonts.googleapis.com/css2?family=Open+Sans:wght@400;600;700&display=swap">
<style>
  :root {
    --backdrop: #2b2b2d;
    --card-dark: #2e2f31;
    --card-dark-edge: #3a3b3e;
    --card-light: #f4f4f5;
    --card-light-edge: #ffffff;
    --brand-blue: #2a8fd0;
    --brand-blue-deep: #1f5f96;
    --ink: #1f1f21;
    --ink-soft: #4a4a4d;
    --on-dark: #e8e8ea;
    --rule: #2b2b2d;
  }
  * { box-sizing: border-box; margin: 0; padding: 0; }
  html, body {
    width: 1200px; height: 997px; overflow: hidden;
    background: var(--backdrop);
    font-family: "Open Sans", Arial, sans-serif;
  }
  .stage {
    position: relative; width: 1200px; height: 997px;
    display: flex; align-items: center; justify-content: center; gap: 60px;
  }
  .card {
    position: relative; width: 520px; height: 300px; border-radius: 24px;
    overflow: hidden;
    box-shadow: 0 18px 40px rgba(0,0,0,.45);
  }

  /* Back side */
  .card--back {
    background: linear-gradient(160deg, var(--card-dark-edge), var(--card-dark));
    color: var(--on-dark);
    display: flex; flex-direction: column; align-items: center;
  }
  .card--back .brand { margin-top: 70px; }
  .card--back .brand-name { color: var(--on-dark); }
  .services-heading {
    margin-top: 46px; font-size: 13px; font-weight: 700; letter-spacing: .5px;
    text-decoration: underline; text-underline-offset: 3px;
  }
  .services-list {
    margin-top: 8px; font-size: 13px; font-weight: 700; letter-spacing: .3px;
    color: var(--brand-blue);
  }

  /* Brand lockup */
  .brand { display: flex; align-items: center; gap: 12px; }
  .brand-mark { width: 26px; height: 26px; background: var(--brand-blue); border-radius: 3px; }
  .brand-name {
    font-size: 20px; font-weight: 700; letter-spacing: 1.5px;
    text-transform: uppercase; color: var(--ink-soft);
  }

  /* Front side */
  .card--front {
    background: linear-gradient(160deg, var(--card-light-edge), var(--card-light));
    color: var(--ink);
  }
  .card--front .brand { position: absolute; top: 46px; left: 0; right: 0; justify-content: center; }
  .details {
    position: absolute; top: 122px; left: 0; right: 0;
    display: flex; justify-content: center; align-items: center; gap: 22px;
  }
  .person { text-align: left; }
  .person-name { font-size: 16px; font-weight: 600; color: var(--brand-blue); }
  .person-role { font-size: 12px; line-height: 1.35; color: var(--ink); }
  .divider {
    width: 2px; height: 62px;
    background: linear-gradient(to bottom, transparent, var(--brand-blue-deep), transparent);
  }
  .contacts { list-style: none; font-size: 12px; line-height: 1.75; }
  .contacts li { display: flex; align-items: center; gap: 9px; }
  .contacts svg { width: 12px; height: 12px; fill: var(--brand-blue-deep); flex: none; }

  .company-rule {
    position: absolute; top: 222px; left: 0; right: 0;
    display: flex; align-items: center;
  }
  .company-rule::before, .company-rule::after {
    content: ""; flex: 1; height: 1.5px; background: var(--rule);
  }
  .company-name {
    padding: 0 8px; font-size: 13px; font-weight: 700; color: var(--brand-blue);
  }
  .company-address {
    position: absolute; top: 243px; left: 0; right: 0; text-align: center;
    font-size: 13px; color: var(--ink);
  }
  .edge-rule {
    position: absolute; bottom: 18px; left: 0; right: 0; height: 1.5px; background: var(--rule);
  }
</style>
</head>
<body>
<main class="stage">

  <section class="card card--back" aria-label="Verso de la carte">
    <div class="brand">
      <span class="brand-mark"></span>
      <span class="brand-name">Corvane Conseil et Registre</span>
    </div>
    <p class="services-heading">OUR SERVICES ARE</p>
    <p class="services-list">ACCOUNTING, TAX, AUDIT AND FINANCIAL MANAGEMENT</p>
  </section>

  <section class="card card--front" aria-label="Recto de la carte">
    <div class="brand">
      <span class="brand-mark"></span>
      <span class="brand-name">Corvane Conseil et Registre</span>
    </div>

    <div class="details">
      <div class="person">
        <p class="person-name">Tomas da Varela</p>
        <p class="person-role">Directeur et Fondateur<br>Expert-comptable diplômé</p>
      </div>
      <span class="divider"></span>
      <ul class="contacts">
        <li>
          <svg viewBox="0 0 24 24" aria-hidden="true"><path d="M6.6 10.8a15.1 15.1 0 0 0 6.6 6.6l2.2-2.2c.3-.3.7-.4 1-.2 1.1.4 2.3.6 3.6.6.6 0 1 .4 1 1V20c0 .6-.4 1-1 1A17 17 0 0 1 3 4c0-.6.4-1 1-1h3.5c.6 0 1 .4 1 1 0 1.3.2 2.5.6 3.6.1.3 0 .7-.2 1l-2.3 2.2z"/></svg>
          <span>022 418 27 35</span>
        </li>
        <li>
          <svg viewBox="0 0 24 24" aria-hidden="true"><path d="M2 5h20v14H2zM3.5 6.5 12 13l8.5-6.5z" fill-rule="evenodd"/></svg>
          <span>tv@corvaneconseil.ch</span>
        </li>
        <li>
          <svg viewBox="0 0 24 24" aria-hidden="true"><path d="M12 2a10 10 0 1 0 0 20 10 10 0 0 0 0-20zm6.9 6h-3a15 15 0 0 0-1.3-3.9A8 8 0 0 1 18.9 8zM12 4c.8 1.2 1.5 2.5 1.9 4h-3.8c.4-1.5 1.1-2.8 1.9-4zM4.3 14a8 8 0 0 1 0-4h3.4a16 16 0 0 0 0 4zm.8 2h3a15 15 0 0 0 1.3 3.9A8 8 0 0 1 5.1 16zm3-8h-3a8 8 0 0 1 4.3-3.9A15 15 0 0 0 8.1 8zM12 20c-.8-1.2-1.5-2.5-1.9-4h3.8c-.4 1.5-1.1 2.8-1.9 4zm2.3-6H9.7a14 14 0 0 1 0-4h4.6a14 14 0 0 1 0 4zm.3 5.9a15 15 0 0 0 1.3-3.9h3a8 8 0 0 1-4.3 3.9zm1.7-5.9a16 16 0 0 0 0-4h3.4a8 8 0 0 1 0 4z"/></svg>
          <span>www.corvaneconseil.ch</span>
        </li>
      </ul>
    </div>

    <div class="company-rule"><span class="company-name">Corvane Advisory and Ledger SA</span></div>
    <p class="company-address">Rue des Vergers-Bleus 14, 1201 Genève</p>
    <span class="edge-rule"></span>
  </section>

</main>
</body>
</html>
```